Blueberry Road side sign

I want a sign to put on the side of the road to advertise the that I have fresh local blueberries for sale. attatched is my company logo.
I want to use the same font that is used in my logo design.
I want "blueberries" written across the sign,
with maybe a couple of berries after the writing.

```html
<!DOCTYPE html>
<html lang="en">
<head>
<meta charset="utf-8">
<title>Fresh Local Blueberries – Roadside Sign</title>
<link rel="stylesheet" href="https://fonts.googleapis.com/css2?family=Alegreya+SC:wght@500&family=Pacifico&family=Libre+Baskerville:wght@700&display=swap">
<style>
  :root {
    --cream: #efeedd;
    --rope: #b98a2e;
    --rope-dark: #7a5716;
    --green: #76901f;
    --sky-blue: #5a8df3;
    --brand-blue: #1f5fb5;
    --berry-dark: #3c4f7a;
    --berry-mid: #6f86b3;
    --leaf: #5e8f3a;
  }
  html, body {
    margin: 0;
    padding: 0;
    width: 1200px;
    height: 600px;
    overflow: hidden;
    background: var(--cream);
  }
  .sign {
    display: block;
    width: 1200px;
    height: 600px;
  }
  .sign-background { fill: var(--cream); }
  .rope-frame {
    fill: none;
    stroke: var(--rope);
    stroke-width: 18;
  }
  .rope-frame-edge {
    fill: none;
    stroke: var(--rope-dark);
    stroke-width: 2;
  }
  .headline {
    font-family: "Alegreya SC", "Times New Roman", serif;
    font-weight: 500;
    font-size: 132px;
    fill: var(--green);
  }
  .product-name {
    font-family: "Pacifico", cursive;
    font-size: 210px;
    fill: var(--sky-blue);
  }
  .brand-mark { fill: var(--brand-blue); }
  .brand-name {
    font-family: "Pacifico", cursive;
    font-size: 58px;
    fill: var(--brand-blue);
  }
  .brand-tagline {
    font-family: "Libre Baskerville", Georgia, serif;
    font-weight: 700;
    font-size: 13px;
    fill: var(--brand-blue);
  }
</style>
</head>
<body>
<svg class="sign" viewBox="0 0 1200 600" xmlns="http://www.w3.org/2000/svg">
  <defs>
    <radialGradient id="berry-photo-tones" cx="50%" cy="45%" r="60%">
      <stop offset="0%" stop-color="#6f86b3"/>
      <stop offset="60%" stop-color="#3c4f7a"/>
      <stop offset="100%" stop-color="#5e8f3a" stop-opacity="0.55"/>
    </radialGradient>
  </defs>

  <rect class="sign-background" x="0" y="0" width="1200" height="600"/>
  <rect class="rope-frame" x="9" y="9" width="1182" height="582"/>
  <rect class="rope-frame-edge" x="18" y="18" width="1164" height="564"/>
  <rect class="rope-frame-edge" x="1" y="1" width="1198" height="598"/>

  <text class="headline" x="42" y="168" textLength="1110" lengthAdjust="spacingAndGlyphs">FRESH LOCAL</text>

  <text class="product-name" x="78" y="390" textLength="1060" lengthAdjust="spacingAndGlyphs">Blueberries</text>

  <ellipse class="berry-photo" cx="440" cy="460" rx="105" ry="85"
           fill="url(#berry-photo-tones)"
           role="img" aria-label="Photo of three fresh blueberries with green leaves"/>

  <g class="brand-lockup">
    <circle class="brand-mark" cx="690" cy="462" r="58"/>
    <text class="brand-name" x="780" y="512">Huon Ridge</text>
    <text class="brand-tagline" x="780" y="540">Tasmanian Blueberries</text>
  </g>
</svg>
</body>
</html>
```